Staffing/Recruitment company

We need to upgrade our website. At the moment we have a template that was built last year and looks not good at all.
We would like to update it with a new design based on what is popular this year. Including some visual effects etc.
This website is to give all information to our potential clients about what we do, clients with worked in the past, how to contact us and about us.
The website consists of 4 pages.
We would like to see a design that uses the color blue.
The current website is https://brightlanestaff.us/
Logo of the company is uploaded

Some designs were not complete...

```html
<!DOCTYPE html>
<html lang="en">
<head>
<meta charset="utf-8">
<title>Brightlane Staff — Staffing & Recruitment</title>
<link href="https://fonts.googleapis.com/css2?family=Bebas+Neue&family=Lato:wght@400;700;900&display=swap" rel="stylesheet">
<style>
:root{
  --navy:#0b0756;
  --navy-soft:#2e2f7c;
  --orange:#f15a24;
  --ink:#1b1b3a;
  --muted:#6b6b78;
  --line:#e3e3e8;
  --field:#f4f4f6;
  --white:#ffffff;
}
*{box-sizing:border-box;margin:0;padding:0}
html,body{width:1200px;height:3532px;overflow:hidden}
body{position:relative;font-family:"Lato",Arial,sans-serif;color:var(--ink);background:var(--white)}
.abs{position:absolute}
a{color:inherit;text-decoration:none}

/* header */
.site-header{left:0;top:0;width:1200px;height:90px;background:#fafafa}
.brand{display:flex;align-items:center;gap:8px;font-weight:900;font-size:16px;letter-spacing:.3px;color:var(--navy)}
.brand-mark{width:30px;height:30px;background:var(--orange)}
.site-header .brand{position:absolute;left:60px;top:30px}
.main-nav{left:444px;top:34px;display:flex;gap:40px;font-size:13px;font-weight:700;color:var(--navy)}
.main-nav .active{color:var(--orange)}
.header-phone{right:60px;top:28px;display:flex;align-items:center;gap:6px;color:var(--orange);font-size:18px;font-weight:700}

/* hero */
.hero{left:0;top:90px;width:1200px;height:585px;overflow:hidden}
.hero-photo{position:absolute;inset:0;background:linear-gradient(120deg,#3d3f8c 0%,#4c4f9c 40%,#383a84 70%,#2f3077 100%)}
.hero-title{position:absolute;left:56px;top:228px;font-family:"Bebas Neue",Impact,sans-serif;font-size:92px;line-height:88px;color:var(--white);letter-spacing:1px}
.hero-title span{color:var(--orange);display:block}
.search{position:absolute;left:60px;top:432px;width:720px;height:61px;display:flex;border-radius:31px;overflow:hidden;background:var(--white)}
.search-input{flex:1;padding-left:34px;display:flex;align-items:center;font-size:15px;color:#555}
.search-btn{width:193px;background:var(--orange);color:var(--white);font-weight:900;font-size:22px;display:flex;align-items:center;justify-content:center}

/* divisions */
.section-title{font-weight:900;color:var(--navy);text-align:center;font-size:38px}
.divisions-title{left:0;top:760px;width:1200px}
.division{top:843px;width:250px;height:250px;background:var(--white);box-shadow:0 0 6px rgba(0,0,0,.12);padding:17px}
.division h3{font-size:16px;font-weight:900;color:var(--navy);margin-bottom:12px}
.division p{font-size:11px;line-height:19.5px;color:var(--muted);height:150px}
.division .more{font-size:11px;font-weight:700;color:var(--orange);display:block;margin-top:30px}

/* career band */
.career{left:0;top:1183px;width:1200px;height:188px;background:var(--navy);color:var(--white)}
.career h2{position:absolute;left:61px;top:50px;font-size:32px;font-weight:900}
.career p{position:absolute;left:61px;top:97px;width:680px;font-size:11.5px;line-height:19px}
.pill{display:flex;align-items:center;justify-content:center;background:var(--orange);color:var(--white);font-weight:900;border-radius:22px}
.career .pill{position:absolute;left:973px;top:76px;width:165px;height:40px;font-size:14px}

/* about */
.about h2{position:absolute;left:61px;top:1495px;font-size:38px;font-weight:900;color:var(--navy)}
.about p{position:absolute;left:61px;top:1555px;width:385px;font-size:11.5px;line-height:19.5px;color:var(--muted)}
.about .pill{position:absolute;left:60px;top:1720px;width:150px;height:41px;font-size:15px}
.about-photo{left:638px;top:1461px;width:562px;height:338px;background:linear-gradient(135deg,#dfe3ea,#b9bfc9 55%,#8d939f)}
.play{left:607px;top:1594px;width:61px;height:61px;border-radius:50%;background:var(--navy)}

/* testimonials */
.testi-band{left:0;top:1916px;width:600px;height:148px;background:var(--navy)}
.testi-photo{top:1984px;height:164px}
.testi h2{position:absolute;left:646px;top:1921px;font-size:31px;font-weight:900;color:var(--navy)}
.testi p{position:absolute;left:646px;top:1970px;width:400px;font-size:11px;line-height:19.5px;color:var(--muted)}
.testi .who{position:absolute;left:646px;top:2055px;font-size:11px;color:var(--orange)}
.arrow-btn{top:2092px;width:38px;height:38px;border-radius:50%}

/* our clients */
.clients{left:0;top:2238px;width:1200px;height:525px;overflow:hidden;background:linear-gradient(110deg,#3b3d8a,#33357f 60%,#2a2b73)}
.clients h2{position:absolute;left:62px;top:80px;font-size:31px;font-weight:900;color:var(--white)}
.client-item{position:absolute;left:105px;display:flex;align-items:center;gap:18px;color:var(--white);font-weight:900;font-size:15px}
.client-item svg{width:50px;height:50px}
.clients .pill{position:absolute;left:61px;top:400px;width:180px;height:40px;font-size:15px}
.portrait{position:absolute;left:738px;top:26px;width:376px;height:376px;border-radius:50%;background:linear-gradient(160deg,#eef0f5,#c9ccd6 60%,#9a9eb0)}

/* request form */
.request-title{left:0;top:2857px;width:1200px;font-size:32px}
.request-sub{left:0;top:2911px;width:1200px;text-align:center;font-size:11.5px;color:var(--muted)}
.field{background:var(--field);border:1px solid var(--line);font-size:11px;color:var(--muted);padding:14px 15px}
.request .pill{position:absolute;left:510px;top:3206px;width:180px;height:40px;font-size:15px}

/* footer */
.site-footer{left:0;top:3337px;width:1200px;height:195px;background:var(--navy);color:var(--white)}
.contact-line{position:absolute;left:61px;display:flex;align-items:center;gap:10px;font-size:11.5px}
.social{position:absolute;top:124px;width:28px;height:28px;border-radius:50%;background:var(--orange)}
.site-footer .brand{position:absolute;left:477px;top:60px;color:var(--white);font-size:18px}
.copyright{position:absolute;left:480px;top:130px;width:240px;text-align:center;font-size:11px;line-height:19px}
.copyright span{color:var(--orange)}
.subscribe-label{position:absolute;right:68px;top:68px;font-size:11.5px;font-weight:700}
.subscribe{position:absolute;left:870px;top:94px;width:270px;height:34px;border:1px solid var(--white);border-radius:17px;display:flex;overflow:hidden;font-size:11px}
.subscribe span{flex:1;padding:10px 16px}
.subscribe b{width:105px;background:var(--white);color:var(--navy);display:flex;align-items:center;justify-content:center;font-size:11px;font-weight:900}
</style>
</head>
<body>

<header class="abs site-header">
  <div class="brand"><span class="brand-mark"></span>BRIGHTLANE STAFF</div>
  <nav class="abs main-nav"><a class="active">Home</a><a>Clients</a><a>About Us</a><a>Contact us</a></nav>
  <div class="abs header-phone">
    <svg width="15" height="15" viewBox="0 0 24 24"><path fill="#f15a24" d="M6.6 10.8a15 15 0 0 0 6.6 6.6l2.2-2.2c.3-.3.7-.4 1-.2 1.1.4 2.3.6 3.6.6.6 0 1 .4 1 1V20c0 .6-.4 1-1 1A17 17 0 0 1 3 4c0-.6.4-1 1-1h3.5c.6 0 1 .4 1 1 0 1.3.2 2.5.6 3.6.1.3 0 .7-.2 1z"/></svg>
    123 456 7890
  </div>
</header>

<section class="abs hero">
  <div class="hero-photo" role="img" aria-label="Team of colleagues working together at computers in a modern office, tinted blue"></div>
  <h1 class="hero-title">HOW SOON CAN<span>YOU START?</span></h1>
  <div class="search"><div class="search-input">Job, Title or keywords</div><div class="search-btn">SEARCH</div></div>
</section>

<h2 class="abs section-title divisions-title">OUR DIVISIONS</h2>
<article class="abs division" style="left:59px">
  <h3>Finance</h3>
  <p>With Wall Street's fast-paced dynamic and ever-changing environment, business demands are always transforming for new and the best talent. Our teams can help alleviate your stresses of recruiting the best...</p>
  <a class="more">READ MORE</a>
</article>
<article class="abs division" style="left:336px">
  <h3>Information Technology</h3>
  <p>The technology of today is not going to be the technology of tomorrow, and keeping up with the constant innovation and change would be a full time job – a job our team wakes up every morning ready to take on...</p>
  <a class="more">READ MORE</a>
</article>
<article class="abs division" style="left:614px">
  <h3>Healthcare</h3>
  <p>Not only do we provide services to the finance and technology world, we also service the healthcare industry with IT professionals as well. We understand the importance of having the right people behind the right projects...</p>
  <a class="more">READ MORE</a>
</article>
<article class="abs division" style="left:891px">
  <h3>Government Projects</h3>
  <p>Navigating the rules and regulations of Government integrators isn't always easy. Our government division, BLGov, recognizes the demands and more importantly, recognizes the solutions. Providing resources in information...</p>
  <a class="more">READ MORE</a>
</article>

<section class="abs career">
  <h2>JOIN OUR CAREER NETWORK</h2>
  <p>Our Career Network will enhance your job search and application process. Whether you choose to apply or just leave your information, we look forward to staying connected with you.</p>
  <a class="pill">JOIN WITH US</a>
</section>

<section class="about">
  <h2>ABOUT US</h2>
  <p>Day in and day out for the last years we've been more than just a staffing company. Throughout this time we've built relationships, we've grown together internally and externally, and have created a system that allows us to personally cater to the needs of our clients and candidates. We've been a mentor for some, a team builder for others, but most importantly we've been there. We know there is no substitute for experience, so let us help you navigate through the ever changing web of talent.</p>
  <a class="pill">READ MORE</a>
  <div class="abs about-photo" role="img" aria-label="Business team meeting in a bright glass-walled office"></div>
  <svg class="abs play" viewBox="0 0 61 61"><circle cx="30.5" cy="30.5" r="30.5" fill="#0b0756"/><path d="M26 22l11 8.5L26 39z" fill="#fff"/></svg>
</section>

<section class="testi">
  <div class="abs testi-band"></div>
  <div class="abs testi-photo" style="left:0;width:92px;background:linear-gradient(135deg,#d9cfc6,#a89a90)" role="img" aria-label="Client portrait, partially visible"></div>
  <div class="abs testi-photo" style="left:125px;width:195px;background:linear-gradient(135deg,#eeeae4,#c9b9a3)" role="img" aria-label="Portrait of a smiling client with glasses"></div>
  <div class="abs testi-photo" style="left:352px;width:195px;background:linear-gradient(135deg,#b7a99a,#4d6a8d)" role="img" aria-label="Portrait of a smiling client in a denim shirt"></div>
  <h2>WHAT OUR CLIENTS SAY</h2>
  <p>Lorem Ipsum is simply dummy text of the printing and typesetting industry. Lorem Ipsum has been the industry's standard dummy text ever since the 1500s, when an unknown printer took a galley of type and scrambled it to make a type specimen book.</p>
  <div class="who">- CLIENT NAME</div>
  <svg class="abs arrow-btn" style="left:655px" viewBox="0 0 38 38"><circle cx="19" cy="19" r="19" fill="#0b0756"/><path d="M22 12l-7 7 7 7" stroke="#fff" stroke-width="2" fill="none"/></svg>
  <svg class="abs arrow-btn" style="left:707px" viewBox="0 0 38 38"><circle cx="19" cy="19" r="19" fill="#f15a24"/><path d="M16 12l7 7-7 7" stroke="#fff" stroke-width="2" fill="none"/></svg>
</section>

<section class="abs clients" role="img" aria-label="Office background tinted blue with a portrait of a smiling woman framed in a magnifier circle">
  <div class="portrait"></div>
  <h2>OUR CLIENTS</h2>
  <div class="client-item" style="top:142px">
    <svg viewBox="0 0 50 50" fill="none" stroke="#f15a24" stroke-width="2"><circle cx="18" cy="10" r="5"/><path d="M10 42V26l8-8 6 10h12M30 28v14M4 22h16M36 16h10v12H36z"/></svg>
    Hire Top Professionals SDETs
  </div>
  <div class="client-item" style="top:217px">
    <svg viewBox="0 0 50 50" fill="none" stroke="#f15a24" stroke-width="2"><circle cx="25" cy="8" r="4"/><path d="M25 12v10M10 22h30M10 22v8M25 22v8M40 22v8"/><circle cx="10" cy="34" r="3"/><circle cx="25" cy="34" r="3"/><circle cx="40" cy="34" r="3"/><path d="M4 46c0-5 12-5 12 0M19 46c0-5 12-5 12 0M34 46c0-5 12-5 12 0"/></svg>
    Let Us Build End To End Automated QA Infrastructure
  </div>
  <div class="client-item" style="top:300px">
    <svg viewBox="0 0 50 50" fill="none" stroke="#f15a24" stroke-width="2"><circle cx="15" cy="10" r="4"/><circle cx="25" cy="8" r="4"/><circle cx="35" cy="10" r="4"/><circle cx="25" cy="24" r="4"/><path d="M8 30v-8h14M42 30v-8H28M17 46V34h16v12M12 46V36M38 46V36"/></svg>
    Request Instructor For Your Team
  </div>
  <a class="pill">REQUEST A CALL</a>
</section>

<section class="request">
  <h2 class="abs section-title request-title">REQUEST A CALL</h2>
  <div class="abs request-sub">Request a call from us to discuss our services and price estimation</div>
  <div class="abs field" style="left:255px;top:2966px;width:337px;height:44px">First Name</div>
  <div class="abs field" style="left:608px;top:2966px;width:337px;height:44px">Last Name</div>
  <div class="abs field" style="left:255px;top:3027px;width:337px;height:44px">Phone No.</div>
  <div class="abs field" style="left:608px;top:3027px;width:337px;height:44px">Services</div>
  <div class="abs field" style="left:255px;top:3087px;width:690px;height:104px">Additional Comments or Preferences</div>
  <a class="pill">REQUEST A CALL</a>
</section>

<footer class="abs site-footer">
  <div class="contact-line" style="top:36px">
    <svg width="12" height="14" viewBox="0 0 24 28"><path fill="#fff" d="M12 0a10 10 0 0 0-10 10c0 7 10 18 10 18s10-11 10-18A10 10 0 0 0 12 0zm0 14a4 4 0 1 1 0-8 4 4 0 0 1 0 8z"/></svg>
    Lorem Ipsum is simply dummy text of the.
  </div>
  <div class="contact-line" style="top:61px">
    <svg width="13" height="13" viewBox="0 0 24 24"><path fill="#fff" d="M6.6 10.8a15 15 0 0 0 6.6 6.6l2.2-2.2c.3-.3.7-.4 1-.2 1.1.4 2.3.6 3.6.6.6 0 1 .4 1 1V20c0 .6-.4 1-1 1A17 17 0 0 1 3 4c0-.6.4-1 1-1h3.5c.6 0 1 .4 1 1 0 1.3.2 2.5.6 3.6.1.3 0 .7-.2 1z"/></svg>
    123 456 7890
  </div>
  <div class="contact-line" style="top:85px">
    <svg width="14" height="11" viewBox="0 0 24 18"><rect x="1" y="1" width="22" height="16" fill="none" stroke="#fff" stroke-width="2"/><path d="M1 1l11 9 11-9" fill="none" stroke="#fff" stroke-width="2"/></svg>
    info@brightlanestaff.us
  </div>
  <span class="social" style="left:60px" aria-label="Social link"></span>
  <span class="social" style="left:98px" aria-label="Social link"></span>
  <span class="social" style="left:136px" aria-label="Social link"></span>
  <div class="brand"><span class="brand-mark"></span>BRIGHTLANE STAFF</div>
  <div class="copyright">© <span>BRIGHTLANE STAFF</span> - 2022. All Rights Reserved.</div>
  <div class="subscribe-label">Subscribe to stay on update.</div>
  <div class="subscribe"><span>Enter email</span><b>SUBSCRIBE</b></div>
</footer>

</body>
</html>
```